Notepads for Marketing pieces-BOLD design

Looking for notepads for marketing pieces with logo, phone number, and website. Maybe something faded in background. Looking for bold and different

```html
<!DOCTYPE html>
<html lang="en">
<head>
<meta charset="utf-8">
<title>Vitalpoint Care Notepads</title>
<link href="https://fonts.googleapis.com/css2?family=Poppins:wght@600;800&family=Open+Sans:wght@400&display=swap" rel="stylesheet">
<style>
  :root {
    --brand-red: #ed1c24;
    --blush: #fdecee;
    --ink: #1a1a1a;
    --paper: #ffffff;
    --backdrop: #eee8e2;
  }
  * { margin: 0; padding: 0; box-sizing: border-box; }
  html, body { width: 1200px; height: 900px; overflow: hidden; background: var(--backdrop); }
  .canvas { position: relative; width: 1200px; height: 900px; }
  .notepad {
    position: absolute; top: 33px; width: 536px; height: 778px;
    background: var(--paper); overflow: hidden;
    box-shadow: 0 3px 8px rgba(0,0,0,0.25);
  }
  .notepad--ruled { left: 39px; }
  .notepad--plain { left: 615px; }
  .notepad__art { position: absolute; inset: 0; width: 100%; height: 100%; }
  .brand-name {
    position: absolute; left: 38px; top: 36px;
    font-family: "Poppins", sans-serif; font-weight: 800; font-size: 21px;
    color: var(--brand-red); letter-spacing: 0.3px; white-space: nowrap;
  }
  .tagline {
    position: absolute; left: 26px; top: 81px;
    font-family: "Poppins", sans-serif; font-weight: 600; font-size: 7.6px;
    color: var(--ink); white-space: nowrap;
  }
  .notepad--plain .brand-name { top: 41px; left: 43px; }
  .notepad--plain .tagline { top: 87px; left: 31px; }
  .contact { position: absolute; left: 379px; top: 25px; list-style: none;
    font-family: "Open Sans", sans-serif; font-size: 10.6px; line-height: 12.4px; color: var(--ink); }
  .contact__item { position: relative; padding-left: 18px; margin-bottom: 4px; }
  .contact__icon { position: absolute; left: 0; top: 1px; width: 13px; height: 13px; }
</style>
</head>
<body>
<main class="canvas">

  <section class="notepad notepad--ruled">
    <svg class="notepad__art" viewBox="0 0 792 1149" preserveAspectRatio="none" aria-hidden="true">
      <path d="M360,0 C470,80 480,190 590,205 C690,218 740,240 792,193" fill="none" stroke="var(--brand-red)" stroke-width="3"/>
      <g stroke="var(--brand-red)" stroke-width="1">
        <line x1="74" y1="272" x2="714" y2="272"/><line x1="74" y1="316" x2="714" y2="316"/>
        <line x1="74" y1="360" x2="714" y2="360"/><line x1="74" y1="404" x2="714" y2="404"/>
        <line x1="74" y1="448" x2="714" y2="448"/><line x1="74" y1="492" x2="714" y2="492"/>
        <line x1="74" y1="536" x2="714" y2="536"/><line x1="74" y1="580" x2="714" y2="580"/>
        <line x1="74" y1="624" x2="714" y2="624"/><line x1="74" y1="668" x2="714" y2="668"/>
        <line x1="74" y1="712" x2="714" y2="712"/><line x1="74" y1="756" x2="714" y2="756"/>
        <line x1="74" y1="800" x2="714" y2="800"/><line x1="74" y1="844" x2="714" y2="844"/>
      </g>
      <path d="M0,888 C120,890 190,950 260,1020 C330,1090 450,1100 792,1000 L792,1149 L0,1149 Z" fill="var(--blush)"/>
      <path d="M0,1002 C250,1130 520,1130 792,982 L792,1149 L0,1149 Z" fill="var(--brand-red)"/>
      <path d="M0,985 C200,1090 520,1140 792,838" fill="none" stroke="var(--brand-red)" stroke-width="3"/>
    </svg>
    <div class="brand-name">VITALPOINT CARE</div>
    <p class="tagline">Home Health | Medical Staffing | Outpatient Therapy</p>
    <ul class="contact">
      <li class="contact__item"><svg class="contact__icon" viewBox="0 0 14 14"><rect x="1" y="3" width="12" height="8" fill="none" stroke="var(--brand-red)" stroke-width="1.3"/><path d="M1,3 L7,8 L13,3" fill="none" stroke="var(--brand-red)" stroke-width="1.3"/></svg>admin@vitalpointcare.org</li>
      <li class="contact__item"><svg class="contact__icon" viewBox="0 0 14 14"><rect x="3.5" y="1" width="7" height="12" rx="1.5" fill="var(--brand-red)"/><circle cx="7" cy="10.5" r="1" fill="#fff"/></svg>555.010.0142<br>555.010.0199</li>
      <li class="contact__item"><svg class="contact__icon" viewBox="0 0 14 14"><path d="M7,13 C3,8 2,6.5 2,5 A5,5 0 0 1 12,5 C12,6.5 11,8 7,13 Z" fill="var(--brand-red)"/><circle cx="7" cy="5" r="1.7" fill="#fff"/></svg>480 Meridian Avenue<br>Fairview, OH 45000</li>
    </ul>
  </section>

  <section class="notepad notepad--plain">
    <svg class="notepad__art" viewBox="0 0 792 1149" preserveAspectRatio="none" aria-hidden="true">
      <path d="M360,0 C470,80 480,190 590,205 C690,218 740,240 792,193" fill="none" stroke="var(--brand-red)" stroke-width="3"/>
      <circle cx="410" cy="570" r="210" fill="var(--blush)"/>
      <path d="M0,815 C120,820 180,880 250,960 C340,1060 500,1110 792,970 L792,1149 L0,1149 Z" fill="var(--blush)"/>
      <path d="M0,1002 C250,1130 520,1130 792,982 L792,1149 L0,1149 Z" fill="var(--brand-red)"/>
      <path d="M0,985 C200,1090 520,1140 792,838" fill="none" stroke="var(--brand-red)" stroke-width="3"/>
    </svg>
    <div class="brand-name">VITALPOINT CARE</div>
    <p class="tagline">Home Health | Medical Staffing | Outpatient Therapy</p>
    <ul class="contact">
      <li class="contact__item"><svg class="contact__icon" viewBox="0 0 14 14"><rect x="1" y="3" width="12" height="8" fill="none" stroke="var(--brand-red)" stroke-width="1.3"/><path d="M1,3 L7,8 L13,3" fill="none" stroke="var(--brand-red)" stroke-width="1.3"/></svg>admin@vitalpointcare.org</li>
      <li class="contact__item"><svg class="contact__icon" viewBox="0 0 14 14"><rect x="3.5" y="1" width="7" height="12" rx="1.5" fill="var(--brand-red)"/><circle cx="7" cy="10.5" r="1" fill="#fff"/></svg>555.010.0142<br>555.010.0199</li>
      <li class="contact__item"><svg class="contact__icon" viewBox="0 0 14 14"><path d="M7,13 C3,8 2,6.5 2,5 A5,5 0 0 1 12,5 C12,6.5 11,8 7,13 Z" fill="var(--brand-red)"/><circle cx="7" cy="5" r="1.7" fill="#fff"/></svg>480 Meridian Avenue<br>Fairview, OH 45000</li>
    </ul>
  </section>

</main>
</body>
</html>
```